Business Card for a Wedding Films Business

We require a business card design for our business 'Lewis Marrow Wedding Films'. The logo needs to look classy and high end.

Target Market(s)

Wedding Couples

Contact Information for Business Card

Lewis Marrow Wedding Films
07312 605 227
films@lewismarrowreels.com
www.lewismarrowreels.com

Facebook: @lewismarrowweddingfilms
Instagram: @lewismarrowfilms

Font styles to use
Sans Serif

Requirements
Must have
• Social media icons - Facebook and Instagram

```html
<!DOCTYPE html>
<html lang="en">
<head>
<meta charset="utf-8">
<title>Lewis Marrow Wedding Films – Business Card</title>
<link href="https://fonts.googleapis.com/css2?family=Jost:wght@400;500&display=swap" rel="stylesheet">
<style>
  :root {
    --page-bg: #ecebe8;
    --ink: #111111;
    --gold: #a68c4a;
    --silver-light: #ffffff;
    --silver-mid: #e4e4e4;
    --silver-deep: #c9c9c9;
    --gold-light: #f3ee9e;
    --gold-mid: #d9cf72;
    --gold-deep: #b2a64c;
  }
  * { box-sizing: border-box; margin: 0; padding: 0; }
  html, body {
    width: 1200px; height: 1200px; overflow: hidden;
    background: var(--page-bg);
    font-family: "Jost", sans-serif;
    color: var(--ink);
  }
  .canvas { position: relative; width: 1200px; height: 1200px; }

  .card {
    position: absolute;
    left: 192px;
    width: 824px;
    height: 470px;
    overflow: hidden;
    box-shadow: 0 10px 28px rgba(0,0,0,0.18);
  }
  .card--front { top: 74px; }
  .card--back  { top: 626px; height: 472px; }

  .card__texture { position: absolute; inset: 0; }
  .card--front .card__texture {
    background:
      radial-gradient(circle at 20% 30%, var(--silver-light) 0, transparent 38%),
      radial-gradient(circle at 80% 70%, var(--silver-light) 0, transparent 40%),
      linear-gradient(135deg, var(--silver-mid), var(--silver-deep) 55%, var(--silver-mid));
  }
  .card--back .card__texture {
    background:
      radial-gradient(circle at 25% 25%, var(--gold-light) 0, transparent 40%),
      radial-gradient(circle at 75% 75%, var(--gold-light) 0, transparent 42%),
      linear-gradient(135deg, var(--gold-mid), var(--gold-deep) 55%, var(--gold-mid));
  }

  .brand { position: absolute; left: 0; right: 0; text-align: center; }
  .brand__mark { display: block; margin: 0 auto; border-radius: 50%; }
  .brand__name { display: block; font-weight: 500; text-transform: uppercase; white-space: nowrap; }
  .brand__tag { display: block; font-weight: 500; text-transform: uppercase; white-space: nowrap; }

  .card--front .brand { top: 44px; }
  .card--front .brand__mark { width: 116px; height: 116px; background: var(--gold); }
  .card--front .brand__name { margin-top: 26px; font-size: 44px; letter-spacing: 0.16em; line-height: 1; }
  .card--front .brand__tag { margin-top: 14px; font-size: 19px; letter-spacing: 0.34em; line-height: 1; }

  .card--back .brand { top: 96px; }
  .card--back .brand__mark { width: 160px; height: 160px; background: var(--ink); }
  .card--back .brand__name { margin-top: 30px; font-size: 54px; letter-spacing: 0.16em; line-height: 1; }
  .card--back .brand__tag { margin-top: 16px; font-size: 24px; letter-spacing: 0.34em; line-height: 1; }

  .contact { position: absolute; font-size: 22px; font-weight: 400; line-height: 1; }
  .contact li { list-style: none; display: flex; align-items: center; height: 36px; white-space: nowrap; }
  .contact__icon { width: 18px; height: 18px; margin-right: 10px; flex: none; }
  .contact--direct { left: 46px; top: 330px; }
  .contact--social { left: 428px; top: 347px; font-size: 21px; }
  .contact--social .contact__icon { width: 18px; height: 18px; background: var(--gold); border-radius: 4px; }

  .divider {
    position: absolute; left: 403px; top: 326px; width: 2px; height: 120px;
    background: linear-gradient(to bottom, transparent, var(--gold) 20%, var(--gold) 80%, transparent);
  }
</style>
</head>
<body>
<div class="canvas">

  <section class="card card--front">
    <div class="card__texture" role="img" aria-label="Soft silver bokeh light pattern"></div>
    <div class="brand">
      <span class="brand__mark"></span>
      <span class="brand__name">Lewis Marrow</span>
      <span class="brand__tag">Wedding Films</span>
    </div>

    <ul class="contact contact--direct">
      <li>
        <svg class="contact__icon" viewBox="0 0 16 16" aria-hidden="true"><path fill="var(--gold)" d="M3.6 1.2l2.2 2.9-1.2 1.7c.9 2 2.6 3.7 4.6 4.6l1.7-1.2 2.9 2.2-1.4 2.3C7.3 13.6 2.4 8.7 1.3 2.6z"/></svg>
        07312 605 227
      </li>
      <li>
        <svg class="contact__icon" viewBox="0 0 16 16" aria-hidden="true"><rect x="1" y="3.5" width="14" height="10" rx="1" fill="var(--gold)"/><path d="M1.5 4.5l6.5 5 6.5-5" stroke="#fff" stroke-width="1.2" fill="none"/></svg>
        films@lewismarrowreels.com
      </li>
      <li>
        <svg class="contact__icon" viewBox="0 0 16 16" aria-hidden="true"><g fill="none" stroke="var(--gold)" stroke-width="1.3"><circle cx="8" cy="8" r="6.5"/><ellipse cx="8" cy="8" rx="3" ry="6.5"/><path d="M1.5 8h13M2.5 4.5h11M2.5 11.5h11"/></g></svg>
        www.lewismarrowreels.com
      </li>
    </ul>

    <div class="divider"></div>

    <ul class="contact contact--social">
      <li><span class="contact__icon" role="img" aria-label="Social page"></span>@lewismarrowweddingfilms</li>
      <li><span class="contact__icon" role="img" aria-label="Photo profile"></span>@lewismarrowfilms</li>
    </ul>
  </section>

  <section class="card card--back">
    <div class="card__texture" role="img" aria-label="Soft golden bokeh light pattern"></div>
    <div class="brand">
      <span class="brand__mark"></span>
      <span class="brand__name">Lewis Marrow</span>
      <span class="brand__tag">Wedding Films</span>
    </div>
  </section>

</div>
</body>
</html>
```